Brovella Web Presence

I need a word press site for my company that houses diverse services, and am looking to profile these areas: Design and Delivery of Social Innovation Initiatives, Innovative Pubic Engagement, The Turquoise Economy, Youth Entrepreneurship, and The Science of Change.

I would also like to profile my recent projects. A blog, video and photos are also important features.

Industry/Entity Type

It Company

Requirements
Must have
• I would like to have an overview of what the company does as a Think, Feel and Do Company, along with sections for specific services and recent project profiles.

I would like a section for a blog

I would like a section for photos and video.

I would like the look and feel of the website to reflect the following:

Maren has spent 30 years leading expeditions into the future. Maren has a special interest in exploring the changing business, social and cultural landscapes and frontiers, uncovering uncharted territory and unleashing hidden potential – within the person, family, organization, community, business or marketplace. Maren thrives on experimentation that has led to blended eastern and western methodologies and technologies that help people and organizations deal with the chronic and tough issues in research-based, intelligent and inspiring ways.

Specialties:Breaking down the walls between disciplines such as environmental, social, and economic approaches to create ideologies and methodologies that weave them all to change the way we live. This ideology and methodology applies to all areas: business development, business identity, strategy for all organizations - public, private and NGO.This starts at the individual level.Maren is also an energy healer specializing in belief reconstruction leading to fulfilling lives.

```html
<!DOCTYPE html>
<html lang="en">
<head>
<meta charset="utf-8">
<title>Brovella</title>
<link href="https://fonts.googleapis.com/css2?family=Bebas+Neue&family=Open+Sans:wght@400;600&display=swap" rel="stylesheet">
<style>
:root{
  --page:#e6ecf6;
  --white:#ffffff;
  --hero:#7399cc;
  --hero-edge:#2f3540;
  --heading:#6f8fc3;
  --nav:#2a5aa8;
  --nav-active:#e0463c;
  --body-text:#666a70;
  --link:#1f5ab8;
  --dot:#4b5565;
  --icon-blue:#4f84bd;
  --icon-rose:#d69a9a;
  --icon-teal:#8cc9c9;
  --video:#0f1a14;
}
*{margin:0;padding:0;box-sizing:border-box}
html,body{width:922px;height:1200px;overflow:hidden;background:var(--page)}
body{position:relative;font-family:Arial,Helvetica,sans-serif;color:var(--body-text)}
.abs{position:absolute}
.site-header{left:0;top:0;width:922px;height:80px;background:var(--white)}
.brand{left:86px;top:22px;display:flex;align-items:center;gap:8px;font-family:'Open Sans',sans-serif;font-size:30px;font-weight:400;color:var(--nav)}
.brand-mark{width:12px;height:12px;border-radius:50%;background:var(--nav-active)}
.main-nav{right:78px;top:35px;display:flex;gap:16px;font-family:'Open Sans',sans-serif;font-weight:600;font-size:9.5px;color:var(--nav);list-style:none}
.main-nav .active{color:var(--nav-active);position:relative}
.main-nav .active::after{content:"";position:absolute;left:50%;top:17px;margin-left:-4px;border:4px solid transparent;border-top:6px solid #222}
.hero{left:0;top:80px;width:922px;height:320px;background:var(--hero);border-bottom:2px solid var(--hero-edge)}
.hero-title{left:100px;top:80px;font-family:'Bebas Neue',sans-serif;font-size:34px;color:var(--white);letter-spacing:.5px}
.hero-sub{left:102px;top:118px;font-family:'Open Sans',sans-serif;font-weight:600;font-size:13.5px;color:var(--white)}
.hero-copy{left:103px;top:174px;font-size:9.4px;line-height:13px;color:var(--white);width:380px}
.hero-dots{left:409px;top:288px;display:flex;gap:7px}
.hero-dots span{width:9px;height:9px;border-radius:50%;background:var(--dot)}
.hero-portrait{left:622px;top:12px;width:196px;height:306px;background:linear-gradient(180deg,#c9b89a 0%,#2a2a2e 38%,#151518 100%);border-radius:60px 60px 0 0}
.service h2{font-family:'Bebas Neue',sans-serif;font-weight:400;font-size:19px;color:var(--heading)}
.service .icon{position:absolute;top:36px;width:43px;height:43px;border-radius:50%}
.service p{position:absolute;top:102px;width:225px;font-size:9.2px;line-height:13.2px}
.service a,.blog-more{color:var(--link);text-decoration:none}
.underline{left:102px;top:462px;width:204px;height:1px;background:var(--heading)}
.underline::after{content:"";position:absolute;left:95px;top:0;border:4px solid transparent;border-top:5px solid var(--heading)}
.section-title{font-family:'Bebas Neue',sans-serif;font-size:19px;color:var(--heading);font-weight:400}
.gallery-arrow{font-family:Arial,sans-serif;font-weight:bold;color:#222;font-size:18px;margin-left:4px}
.gallery-item{top:654px;height:121px;border:3px solid var(--white)}
.video{left:101px;top:844px;width:419px;height:235px;background:radial-gradient(circle at 60% 45%,#3a6a7a 0%,#16302c 45%,var(--video) 100%)}
.video-bar{position:absolute;left:6px;right:6px;bottom:6px;height:14px;background:rgba(0,0,0,.7)}
.video-bar svg{position:absolute;left:10px;top:3px}
.video-bar i{position:absolute;left:40px;right:60px;top:6px;height:2px;background:#555}
.post{left:547px;width:300px;height:70px}
.post .thumb{position:absolute;left:0;top:0;width:63px;height:36px}
.post p{position:absolute;left:74px;top:-2px;width:220px;font-size:9.2px;line-height:13px}
.post small{position:absolute;left:0;top:46px;font-size:8px}
.blog-more{left:547px;top:1049px;font-size:9.5px}
.site-footer{left:0;top:1136px;width:922px;height:64px;background:var(--hero);color:var(--white)}
.legal{left:102px;top:17px;font-size:9px;line-height:11px}
.social{left:732px;top:19px;display:flex;align-items:center;gap:5px;font-size:8px}
.social span{width:24px;height:24px;border-radius:3px}
</style>
</head>
<body>
<header class="site-header abs">
  <div class="brand abs"><span class="brand-mark"></span>Brovella</div>
  <ul class="main-nav abs">
    <li class="active">HOME</li><li>ABOUT US</li><li>SERVICES</li><li>GALLERY</li><li>BLOG</li><li>TESTIMONIALS</li><li>CONTACT US</li>
  </ul>
</header>

<section class="hero abs">
  <h1 class="hero-title abs">SOCIAL INNOVATION INITIATIVES</h1>
  <p class="hero-sub abs">LOREM IPSUM DOLOR SIT AMET, CONSECTETUER ADIPI</p>
  <p class="hero-copy abs">Lorem ipsum dolor sit amet, consectetuer adipiscing elit. Prent estibulum molestie lacus.<br>Aenean nonummy hendrerit mauris. Phasellus porta. Fusce suscipit varius mi.<br>Cum sociis natoque penatibus. et magnis dis parturient montes, nascetur ridiculus mus.<br>Nulla dui. Fusce feugiat malesuada odio.</p>
  <div class="hero-dots abs"><span></span><span></span><span></span><span></span><span></span><span></span></div>
  <div class="hero-portrait abs" role="img" aria-label="Portrait photo of a businesswoman in a dark suit, arms crossed"></div>
</section>

<article class="service abs" style="left:102px;top:436px">
  <h2>SOCIAL INNOVATION INITIATIVES</h2>
  <span class="icon" style="left:78px;background:var(--icon-blue)"><svg width="43" height="43" viewBox="0 0 43 43"><rect x="11" y="13" width="16" height="11" rx="3" fill="#fff"/><rect x="17" y="18" width="15" height="10" rx="3" fill="#fff" stroke="var(--icon-blue)" stroke-width="1.5"/></svg></span>
  <p>Lorem ipsum dolor sit amet, consectetuer adipiscingt. Prent estibulum molestie lacus. Aenean nonummy hendrerit mauris. Phasellus porta. Fusce suscipit var Cum sociis natoque penatibus. <a href="#">Know more</a></p>
</article>
<div class="underline abs"></div>
<article class="service abs" style="left:365px;top:436px">
  <h2>INNOVATIVE PUBIC ENGAGEMENT</h2>
  <span class="icon" style="left:88px;background:var(--icon-rose)"><svg width="43" height="43" viewBox="0 0 43 43"><rect x="13" y="13" width="17" height="12" rx="1" fill="none" stroke="#fff" stroke-width="2"/><rect x="19" y="27" width="5" height="3" fill="#fff"/></svg></span>
  <p>Lorem ipsum dolor sit amet, consectetuer adipiscingt. Prent estibulum molestie lacus. Aenean nonummy hendrerit mauris. Phasellus porta. Fusce suscipit var Cum sociis natoque penatibus. <a href="#">Know more</a></p>
</article>
<article class="service abs" style="left:626px;top:436px">
  <h2>YOUTH ENTREPRENEURSHIP</h2>
  <span class="icon" style="left:64px;background:var(--icon-teal)"><svg width="43" height="43" viewBox="0 0 43 43"><circle cx="21.5" cy="17" r="5" fill="#fff"/><path d="M12 31c0-6 4-8 9.5-8s9.5 2 9.5 8z" fill="#fff"/></svg></span>
  <p style="left:-6px">Lorem ipsum dolor sit amet, consectetuer adipiscingt. Prent estibulum molestie lacus. Aenean nonummy hendrerit mauris. Phasellus porta. Fusce suscipit var Cum sociis natoque penatibus. <a href="#">Know more</a></p>
</article>

<h2 class="section-title abs" style="left:100px;top:656px">PHOTO GALLERY<span class="gallery-arrow">»</span></h2>
<div class="gallery-item abs" style="left:261px;width:186px;background:linear-gradient(135deg,#1d3a4a,#8fb7a8 50%,#2a4a5a)" role="img" aria-label="Glowing network globe held in hands"></div>
<div class="gallery-item abs" style="left:459px;width:187px;background:linear-gradient(135deg,#f2f2f2,#e8d070 55%,#dcdcdc)" role="img" aria-label="Website screenshot with a colourful bird illustration"></div>
<div class="gallery-item abs" style="left:656px;width:187px;background:linear-gradient(160deg,#f5d9a0,#f0c070 45%,#b89a80)" role="img" aria-label="Sunlit sea seen from the deck of a boat"></div>

<h2 class="section-title abs" style="left:101px;top:804px">VIDEO GALLERY</h2>
<div class="video abs" role="img" aria-label="Video still of a man with a headlamp in a lit tunnel">
  <div class="video-bar"><svg width="8" height="8" viewBox="0 0 8 8"><path d="M0 0l8 4-8 4z" fill="#fff"/></svg><i></i></div>
</div>

<h2 class="section-title abs" style="left:547px;top:804px">LATEST FROM THE BLOGS</h2>
<div class="post abs" style="top:848px"><div class="thumb" style="background:linear-gradient(90deg,#b0204a,#e0502a,#e8a030,#6a2a8a)" role="img" aria-label="Colourful striped blog thumbnail"></div><p>Lorem ipsum dolor sit amet, consectetuer adipiscin Prent estibulum molestie lacus. Aenean nonum hendrerit mauris.</p><small>Posted March 28th at 21:0145</small></div>
<div class="post abs" style="top:919px"><div class="thumb" style="background:linear-gradient(180deg,#c8243a,#a01830)" role="img" aria-label="Red event banner thumbnail"></div><p>Lorem ipsum dolor sit amet, consectetuer adipiscin Prent estibulum molestie lacus. Aenean nonum hendrerit mauris.</p><small>Posted March 28th at 21:0145</small></div>
<div class="post abs" style="top:990px"><div class="thumb" style="background:linear-gradient(90deg,#f0f0f0,#40b060,#e0c030,#3070c0)" role="img" aria-label="Colourful abstract typography thumbnail"></div><p>Lorem ipsum dolor sit amet, consectetuer adipiscin Prent estibulum molestie lacus. Aenean nonum hendrerit mauris.</p><small>Posted March 28th at 21:0145</small></div>
<a class="blog-more abs" href="#">Read all posts</a>

<footer class="site-footer abs">
  <p class="legal abs">COPYRIGHT 2013. ALL RIGHTS RESERVED.<br>TERMS &amp; CONDITIONS &nbsp;- &nbsp;PRIVACY &nbsp;- &nbsp;DISCLAIMER</p>
  <div class="social abs">X3 &nbsp;<span style="background:#4ab3e8"></span><span style="background:#c8302a"></span><span style="background:#3b5998"></span></div>
</footer>
</body>
</html>
```